High end wine label at Austrian Winery

We are a traditional winery in Austria in region Burgenland. We are looking for a relaunch of our current wine label for our [solstice] series. It's a high end wine series at an upper price range. At the moment we have just two kinds of the label, one white one for the white wines and one black one for the red wines. This is a series of wine, white, red, sweet, sparkling and a top wine categories. So we need the same label, but in 4 different ways to distinguish the wines plus the sparkling. Maybe in color, patterns, ... or something else. The label should be very simple, including our new logo. It's also possible to make one label but we can splitting two parts of the label. The size of the label does not matter, need not be the same as now. It's a bit higher than a normal bottle. Additionally we need a back label with wine description and the wine dates on it.

Target Market(s)

private consumers and restaurants, no retailers

Colors

Designer to choose colors to be used in the design.

Requirements
Must have
• simple label with 4 different categories (red, white, sweet, top) plus Frizzante label, new logo integrated, high end label. Just logo, grape variety and [solstice] as text on the front label as text
Nice to have
• It's just good, if there'sa possibility to have different colors of each grape variety (about 10 different), but all the same style. top Wines should have an extraordinary design, but familiar with the others
Should not have
• no cheap look

```html
<!DOCTYPE html>
<html lang="en">
<head>
<meta charset="utf-8">
<title>Halden Frizzante – Front Label</title>
<link rel="stylesheet" href="https://fonts.googleapis.com/css2?family=Big+Shoulders+Display:wght@200;400&family=Great+Vibes&family=Montserrat:wght@500;600&display=swap">
<style>
  :root {
    --backdrop: #e4e3da;
    --label-black: #1b1b1c;
    --label-black-edge: #101011;
    --band-red: #c8100e;
    --band-red-dark: #8e0707;
    --script-red: #5e0404;
    --accent-red: #b3121a;
    --ink-white: #f2f2f0;
    --ink-grey: #c9c9c6;
    --gold: #d6a21e;
    --grape-red: #9a1b1d;
  }
  * { margin: 0; padding: 0; box-sizing: border-box; }
  html, body { width: 886px; height: 1200px; overflow: hidden; }
  body { background: var(--backdrop); position: relative; font-family: "Montserrat", sans-serif; }

  .label { position: absolute; left: 183px; top: 48px; width: 520px; height: 1096px; }

  .band { position: absolute; }
  .band svg { position: absolute; inset: 0; width: 100%; height: 100%; }
  .band-top { left: 35px; top: 0; width: 430px; height: 90px; }
  .band-bottom { left: 67px; top: 1005px; width: 430px; height: 91px; }
  .band-copy {
    position: absolute; left: 20px; right: 20px; display: flex; flex-direction: column;
    font-family: "Great Vibes", cursive; font-size: 16px; line-height: 18px; color: var(--script-red);
    white-space: nowrap; text-align: center;
  }
  .band-top .band-copy { top: 10px; }
  .band-bottom .band-copy { top: 18px; }

  .panel {
    position: absolute; left: 0; top: 72px; width: 520px; height: 928px;
    background: linear-gradient(90deg, var(--label-black-edge), var(--label-black) 12%, var(--label-black) 88%, var(--label-black-edge));
  }

  .brand-name {
    position: absolute; left: 0; right: 0; top: 186px; text-align: center;
    font-weight: 600; font-size: 27px; letter-spacing: 4px; color: var(--ink-white); line-height: 1;
  }

  .grape-art {
    position: absolute; left: 162px; top: 248px; width: 200px; height: 196px; border-radius: 50%;
    background: radial-gradient(ellipse at 45% 50%, rgba(154,27,29,0.5), rgba(154,27,29,0.1) 75%, transparent);
  }

  .wine-name {
    position: absolute; left: 0; right: 0; top: 470px; text-align: center;
    font-family: "Big Shoulders Display", sans-serif; font-weight: 200; font-size: 150px; line-height: 1;
    color: var(--ink-white); letter-spacing: 1px;
  }
  .wine-name .accent { color: var(--accent-red); font-weight: 400; }

  .wine-type {
    position: absolute; left: 0; right: 0; top: 668px; text-align: center;
    font-family: "Great Vibes", cursive; font-size: 60px; color: var(--accent-red); line-height: 1;
    word-spacing: 12px;
  }
  .series {
    position: absolute; left: 0; right: 0; top: 738px; text-align: center;
    font-size: 19px; font-weight: 500; letter-spacing: 1px; color: var(--gold); text-transform: uppercase;
  }

  .spec {
    position: absolute; top: 800px; font-family: "Big Shoulders Display", sans-serif; font-weight: 400;
    font-size: 22px; color: var(--ink-grey);
  }
  .spec-vol { left: 56px; }
  .spec-size { right: 46px; }
</style>
</head>
<body>
  <main class="label">
    <div class="band band-top">
      <svg viewBox="0 0 430 90" preserveAspectRatio="none" aria-hidden="true">
        <defs>
          <linearGradient id="bandRed" x1="0" x2="1">
            <stop offset="0" stop-color="#8e0707"/>
            <stop offset="0.5" stop-color="#c8100e"/>
            <stop offset="1" stop-color="#8e0707"/>
          </linearGradient>
        </defs>
        <path d="M4 14 L120 8 L260 12 L426 4 L422 40 L428 86 L300 82 L140 88 L2 84 L8 48 Z" fill="url(#bandRed)"/>
      </svg>
      <div class="band-copy">
        <span>Grown on sunny slopes by the lake shore</span>
        <span>picked by hand and pressed with quiet care</span>
        <span>for a long evening among good friends</span>
      </div>
    </div>

    <section class="panel">
      <div class="brand-name">HALDEN</div>

      <div class="grape-art" role="img" aria-label="Red line illustration of a grape bunch with a vine leaf"></div>

      <h1 class="wine-name">FRIZZ<span class="accent">A</span>NTE</h1>
      <p class="wine-type">Red Wine</p>
      <p class="series">[solstice]</p>

      <span class="spec spec-vol">9% VOL</span>
      <span class="spec spec-size">750ML</span>
    </section>

    <div class="band band-bottom">
      <svg viewBox="0 0 430 91" preserveAspectRatio="none" aria-hidden="true">
        <path d="M2 6 L150 2 L300 8 L428 4 L424 46 L428 84 L260 88 L110 84 L4 90 L8 44 Z" fill="url(#bandRed)"/>
      </svg>
      <div class="band-copy">
        <span>Bright cherry notes with a lively sparkle</span>
        <span>best served cool beside simple food</span>
        <span>a gift of the warm valley</span>
      </div>
    </div>
  </main>
</body>
</html>
```